Tallow Crest Software PowerPoint template

We are a software company selling endpoint visibility, access and security technology to enterprise-level IT departments.
Our technology helps organizations gain comprehensive visibility into and control over devices accessing their corporate network so they can quickly identify and address suspicious activity on the network that could lead to potential threats like data breaches.
This technology can cost organizations upwards of $1M - depending on the size of the organization. Our primary clients are Meridane 2,000 companies.
We want a professional, polished PowerPoint template that we can use for all company presentations. Please include:
Title page
Section page
General info page
Thank you page
Logo options and color specs are attached.
Please include our tagline on at least the title page: Discover the edge. Optimize the whole.

```html
<!DOCTYPE html>
<html lang="en">
<head>
<meta charset="utf-8">
<title>Tallow Crest Software – Presentation Template</title>
<link rel="stylesheet" href="https://fonts.googleapis.com/css2?family=Montserrat:wght@300;400;500;600;700;800&display=swap">
<style>
:root{
  --stage:#c9c9c9;
  --maroon:#7a2323;
  --copper:#b9765a;
  --copper-light:#c98a6c;
  --ink:#2e2e2e;
  --slate:#5a5a5a;
  --grey:#787878;
  --white:#ffffff;
}
*{box-sizing:border-box;margin:0;padding:0}
html,body{width:1200px;height:621px;overflow:hidden;background:var(--stage);font-family:"Montserrat",Arial,sans-serif;color:var(--ink)}
.canvas{position:relative;width:1200px;height:621px}
.slide{position:absolute;width:380px;height:282px;overflow:hidden;background:linear-gradient(160deg,#fafafa 0%,#ececec 100%)}
.s-title{left:17px;top:20px;background:var(--white)}
.s-agenda{left:411px;top:20px}
.s-stats{left:805px;top:20px}
.s-timeline{left:17px;top:320px;height:283px}
.s-table{left:411px;top:320px;height:283px}
.s-questions{left:805px;top:320px;height:283px;background:linear-gradient(135deg,#b8735a 0%,#95443a 45%,#7a2222 100%)}

.section-tag{position:absolute;left:0;top:14px;height:11px;padding:0 16px 0 8px;background:var(--white);border-radius:0 6px 6px 0;font-size:5.5px;letter-spacing:.5px;color:#8a8a8a;line-height:11px}

.footer{position:absolute;left:0;bottom:0;width:100%;height:23px;background:linear-gradient(90deg,#6e1f1f 0%,#8c3a30 60%,#9b4a3a 100%);display:flex;align-items:center;padding:0 8px 0 12px}
.brand{display:flex;align-items:center;gap:4px;font-size:5.5px;font-weight:600;letter-spacing:1px;color:var(--white);text-transform:uppercase;line-height:1}
.brand-mark{width:7px;height:7px;background:var(--white)}
.tagline{margin-left:auto;font-size:5.5px;color:var(--white);font-weight:400}
.tagline b{font-weight:700}
.page-num{margin-left:8px;width:13px;height:13px;border:1px solid rgba(255,255,255,.7);border-radius:50%;font-size:6px;color:var(--white);display:flex;align-items:center;justify-content:center}

/* title slide */
.hero-photo{position:absolute;left:81px;top:0;width:299px;height:164px;background:linear-gradient(160deg,#3b5d8c 0%,#7f6a5c 40%,#c9874c 60%,#3a3040 100%)}
.title-logo{position:absolute;left:81px;top:0;width:147px;height:46px;background:var(--white);display:flex;align-items:center;justify-content:center;gap:6px;font-size:8px;font-weight:600;letter-spacing:1.5px;color:var(--maroon);text-transform:uppercase}
.title-logo .brand-mark{width:9px;height:9px;background:var(--copper)}
.title-band{position:absolute;left:81px;top:164px;width:299px;height:19px;background:linear-gradient(90deg,#7a2323,#8b3030);color:var(--white);font-size:6px;font-weight:600;letter-spacing:.6px;padding-left:34px;line-height:19px}
.title-head{position:absolute;left:114px;top:195px;width:230px;font-size:14.5px;font-weight:300;line-height:1.08;color:#a0403a}
.title-date{position:absolute;left:114px;top:230px;font-size:4.5px;color:var(--slate)}
.title-tagline{position:absolute;left:114px;top:257px;font-size:6.5px;color:var(--slate)}
.title-tagline b{color:var(--maroon);font-weight:700}

/* agenda */
.agenda-title{position:absolute;left:43px;top:52px;font-size:24px;font-weight:700;color:#1f1f1f}
.agenda-list{position:absolute;left:45px;top:96px;width:220px;list-style:none}
.agenda-list li{position:relative;padding-left:18px;font-size:7.5px;line-height:1.6;color:var(--slate);margin-bottom:6px}
.agenda-list li::before{content:"";position:absolute;left:0;top:3px;width:9px;height:6px;background:var(--copper);clip-path:polygon(0 0,70% 0,100% 50%,70% 100%,0 100%)}

/* headings */
.slide-heading{position:absolute;left:30px;top:44px;font-size:14.5px;font-weight:300;color:#333}
.slide-heading b{font-weight:700}

/* stats */
.stat{position:absolute;top:72px;width:82px}
.stat-ring{display:block;margin:0 auto}
.stat-card{position:relative;margin-top:8px;height:50px;background:var(--grey);padding:6px 9px;color:var(--white)}
.stat-card::before{content:"";position:absolute;left:50%;top:-6px;margin-left:-6px;border:6px solid transparent;border-top:0;border-bottom-color:var(--grey)}
.stat-card p{font-size:7px;line-height:1.2}
.stat-card small{position:absolute;left:9px;bottom:5px;font-size:3.6px}
.stats-note{position:absolute;left:46px;top:214px;width:300px;font-size:7.5px;line-height:1.3;color:#444}

/* timeline */
.figures{position:absolute;left:30px;top:82px;width:324px;height:38px;background:linear-gradient(180deg,rgba(90,90,90,0) 0%,rgba(90,90,90,.18) 100%)}
.eras{position:absolute;left:30px;top:120px;width:324px;display:flex}
.era{flex:1}
.era-name{height:30px;display:flex;align-items:center;justify-content:center;text-align:center;font-size:6.8px;font-weight:700;color:var(--white);line-height:1.15;text-transform:uppercase}
.era-years{height:16px;background:#e2e2e2;text-align:center;font-size:5.5px;line-height:16px;color:var(--slate);letter-spacing:.3px}
.era-text{padding:8px 8px 0;font-size:6px;line-height:1.3;color:var(--slate)}
.era.spam .era-name{background:var(--grey)}
.era.search .era-name{background:var(--copper)}
.era.search .era-text{color:var(--copper)}
.era.social .era-name{background:var(--maroon)}
.era.social .era-text{color:var(--maroon)}
.era.mobile .era-name{background:var(--ink)}

/* table */
.attack-table{position:absolute;left:32px;top:77px;width:317px;border-collapse:collapse}
.attack-table th{background:#9a9a9a;color:var(--white);font-size:4px;font-weight:600;letter-spacing:.4px;height:11px;text-transform:uppercase}
.attack-table td{vertical-align:middle;text-align:center}
.attack-table .row-2005 td{height:66px;background:#e6e6e6}
.attack-table .row-2015 td{height:62px;background:#ededed}
.attack-table .size{width:80px;font-size:14px;font-weight:300;color:#999;line-height:.9}
.attack-table .size span{display:block;font-size:7px;color:#a7a7a7}
.attack-table .row-2005 .size,.attack-table .row-2005 .size span{color:var(--copper-light)}
.attack-table .type{width:146px;border-left:1px solid #f8f8f8;border-right:1px solid #f8f8f8}
.attack-table .concern{font-size:4px;color:var(--slate)}
.type-wrap{display:flex;align-items:center;justify-content:center;gap:6px}
.pct{text-align:left;font-size:12px;font-weight:700;color:var(--copper)}
.row-2015 .pct{color:var(--ink)}
.pct span{font-size:7px}
.pct small{display:block;font-size:3.6px;font-weight:400;color:var(--slate)}
.year-label{position:absolute;left:14px;font-size:7px;font-weight:700;transform:rotate(-90deg);transform-origin:left top}
.y2005{top:128px;color:#777}
.y2015{top:196px;color:var(--maroon)}
.table-note{position:absolute;left:44px;top:218px;width:300px;font-size:6.5px;line-height:1.3;color:var(--slate)}

/* questions */
.q-head{position:absolute;left:40px;top:40px;font-size:45px;font-weight:800;line-height:.86;color:var(--white);letter-spacing:-.5px}
.q-device{position:absolute;left:262px;top:145px}
.q-contacts{position:absolute;left:256px;top:212px;list-style:none;width:100px}
.q-contacts li{display:flex;gap:5px;align-items:flex-start;padding:3px 0;border-top:1px solid rgba(255,255,255,.3);color:var(--white)}
.q-contacts li:first-child{border-top:0}
.q-icon{width:8px;height:8px;background:rgba(255,255,255,.9);flex:none;margin-top:1px}
.q-contacts b{display:block;font-size:5px;font-weight:700;letter-spacing:.4px}
.q-contacts span{display:block;font-size:4.2px;opacity:.85}
</style>
</head>
<body>
<main class="canvas">

  <section class="slide s-title">
    <div class="hero-photo" role="img" aria-label="Night city skyline with glowing light trails of traffic"></div>
    <div class="title-logo"><span class="brand-mark"></span>Tallow Crest Software</div>
    <div class="title-band">SECURITY AND COMPLIANCE</div>
    <h1 class="title-head">Protect your wireless network and your critical data.</h1>
    <p class="title-date">February 14, 2015</p>
    <p class="title-tagline"><b>Discover</b> the edge. <b>Optimize</b> the whole.</p>
  </section>

  <section class="slide s-agenda">
    <div class="section-tag">SECURITY AND COMPLIANCE</div>
    <h2 class="agenda-title">Agenda</h2>
    <ul class="agenda-list">
      <li>Pellentesque et sem tempor, dictum velit nec, dictum sem.</li>
      <li>Mauris lacinia lectus ut tincidunt suscipit.</li>
      <li>Proin luctus nibh sit amet adipiscing euismod.</li>
      <li>Curabitur at turpis semper, blandit magna vel, malesuada ligula.</li>
    </ul>
    <footer class="footer"><span class="brand"><span class="brand-mark"></span>Tallow Crest Software</span><span class="tagline"><b>Discover</b> the edge. <b>Optimize</b> the whole.</span><span class="page-num">1</span></footer>
  </section>

  <section class="slide s-stats">
    <div class="section-tag">SECURITY AND COMPLIANCE</div>
    <h2 class="slide-heading">Lorem Ipsum is that <b>established</b></h2>
    <div class="stat" style="left:46px">
      <svg class="stat-ring" width="62" height="62" viewBox="0 0 62 62"><circle cx="31" cy="31" r="28" fill="none" stroke="#d6d6d6" stroke-width="5"/><circle cx="31" cy="31" r="28" fill="none" stroke="#b9765a" stroke-width="5" stroke-dasharray="140 176" transform="rotate(-90 31 31)"/><circle cx="31" cy="31" r="23" fill="#555"/><text x="31" y="29" text-anchor="middle" fill="#fff" font-size="6.5" font-weight="700" font-family="Montserrat,sans-serif">5% to 20%</text><text x="31" y="37" text-anchor="middle" fill="#fff" font-size="6.5" font-weight="700" font-family="Montserrat,sans-serif">Lorem</text></svg>
      <div class="stat-card"><p>Lorem Ipsum is simply dummy text of the</p><small>SA long established fact that</small></div>
    </div>
    <div class="stat" style="left:149px">
      <svg class="stat-ring" width="62" height="62" viewBox="0 0 62 62"><circle cx="31" cy="31" r="28" fill="none" stroke="#d6d6d6" stroke-width="5"/><circle cx="31" cy="31" r="28" fill="none" stroke="#b9765a" stroke-width="5" stroke-dasharray="130 176" transform="rotate(-90 31 31)"/><circle cx="31" cy="31" r="23" fill="#555"/><text x="31" y="29" text-anchor="middle" fill="#fff" font-size="6.5" font-weight="700" font-family="Montserrat,sans-serif">+27%</text><text x="31" y="37" text-anchor="middle" fill="#fff" font-size="6.5" font-weight="700" font-family="Montserrat,sans-serif">productivity</text></svg>
      <div class="stat-card"><p>Printing and typesetting industry.</p><small>Long established fact that a reader</small></div>
    </div>
    <div class="stat" style="left:252px">
      <svg class="stat-ring" width="62" height="62" viewBox="0 0 62 62"><circle cx="31" cy="31" r="28" fill="none" stroke="#b9765a" stroke-width="5"/><circle cx="31" cy="31" r="23" fill="#555"/><text x="31" y="29" text-anchor="middle" fill="#fff" font-size="6.5" font-weight="700" font-family="Montserrat,sans-serif">$19</text><text x="31" y="37" text-anchor="middle" fill="#fff" font-size="6.5" font-weight="700" font-family="Montserrat,sans-serif">billion</text></svg>
      <div class="stat-card"><p>Contrary to popular belief, Lorem Ipsum</p><small>Non-characteristic words etc.</small></div>
    </div>
    <p class="stats-note">There are many variations of passages of Lorem Ipsum available, but the majority have suffered alteration in some form.</p>
    <footer class="footer"><span class="brand"><span class="brand-mark"></span>Tallow Crest Software</span><span class="tagline"><b>Discover</b> the edge. <b>Optimize</b> the whole.</span><span class="page-num">3</span></footer>
  </section>

  <section class="slide s-timeline">
    <div class="section-tag">SECURITY AND COMPLIANCE</div>
    <h2 class="slide-heading">Lorem Ipsum is simply <b>of the printing</b></h2>
    <div class="figures" role="img" aria-label="Silhouette figures for each era: fishing, searching, broadcasting and using a phone"></div>
    <div class="eras">
      <div class="era spam"><div class="era-name">Spam and<br>phishing sites</div><div class="era-years">EARLY 2000–2009</div><p class="era-text">Lorem Ipsum is simply dummy text of the printing and typesetting industry.</p></div>
      <div class="era search"><div class="era-name">Search<br>engines</div><div class="era-years">2009–2011</div><p class="era-text">Curabitur aliquet quam a libero vulputate gravida.</p></div>
      <div class="era social"><div class="era-name">Social<br>media</div><div class="era-years">2011–2015</div><p class="era-text">Cras non lorem et ipsum commodo aliquet.</p></div>
      <div class="era mobile"><div class="era-name">Mobile</div><div class="era-years">2015–</div><p class="era-text">Sed mollis tortor auctor, malesuada ipsum vel, scelerisque tellus.</p></div>
    </div>
    <footer class="footer"><span class="brand"><span class="brand-mark"></span>Tallow Crest Software</span><span class="tagline"><b>Discover</b> the edge. <b>Optimize</b> the whole.</span><span class="page-num">2</span></footer>
  </section>

  <section class="slide s-table">
    <div class="section-tag">SECURITY AND COMPLIANCE</div>
    <h2 class="slide-heading">Nam et nisi dapibus, <b>mollis lacus.</b></h2>
    <span class="year-label y2005">2005</span>
    <span class="year-label y2015">2015</span>
    <table class="attack-table">
      <tr><th>Largest attack size</th><th>Most prominent attack type</th><th>Top concerns</th></tr>
      <tr class="row-2005">
        <td class="size">8<span>Gbps</span></td>
        <td class="type"><div class="type-wrap">
          <svg width="52" height="20" viewBox="0 0 52 20"><g fill="#b9765a"><circle cx="5" cy="5" r="4"/><circle cx="15" cy="5" r="4"/><circle cx="25" cy="5" r="4"/><circle cx="35" cy="5" r="4"/><circle cx="45" cy="5" r="4"/><circle cx="5" cy="15" r="4"/><circle cx="15" cy="15" r="4"/><circle cx="25" cy="15" r="4"/><circle cx="35" cy="15" r="4"/></g><circle cx="45" cy="15" r="4" fill="#c4c4c4"/></svg>
          <div class="pct">90<span>%</span><small>of respondents cited</small></div></div></td>
        <td class="concern"><svg width="50" height="22" viewBox="0 0 50 22"><polygon points="9,1 3,12 8,12 5,21 14,8 9,8 12,1" fill="#666"/><text x="22" y="15" font-size="12" fill="#b9765a" font-family="Montserrat,sans-serif" font-weight="700">+</text><path d="M34 18 q0 -6 4 -6 q4 0 4 -5 q0 -5 4 -5" fill="none" stroke="#666" stroke-width="2.5" stroke-linecap="round"/></svg><br>DDoS Attacks &nbsp;&nbsp;&nbsp;&nbsp; Worms</td>
      </tr>
      <tr class="row-2015">
        <td class="size">400<span>Gbps</span></td>
        <td class="type"><div class="type-wrap">
          <svg width="52" height="20" viewBox="0 0 52 20"><g fill="#555"><circle cx="5" cy="5" r="4"/><circle cx="15" cy="5" r="4"/><circle cx="25" cy="5" r="4"/><circle cx="35" cy="5" r="4"/><circle cx="5" cy="15" r="4"/><circle cx="15" cy="15" r="4"/><circle cx="25" cy="15" r="4"/></g><g fill="#c4c4c4"><circle cx="45" cy="5" r="4"/><circle cx="35" cy="15" r="4"/><circle cx="45" cy="15" r="4"/></g></svg>
          <div class="pct">65<span>%</span><small>of all attacks were</small></div></div></td>
        <td class="concern"><svg width="16" height="22" viewBox="0 0 16 22"><polygon points="9,1 3,12 8,12 5,21 14,8 9,8 12,1" fill="#b9765a"/></svg><br>DDoS Attacks</td>
      </tr>
    </table>
    <p class="table-note">Sed mollis tortor auctor, malesuada ipsum vel, scelerisque tellus.<br>Nam et nisi dapibus, fringilla tortor et, mollis lacus.</p>
    <footer class="footer"><span class="brand"><span class="brand-mark"></span>Tallow Crest Software</span><span class="tagline"><b>Discover</b> the edge. <b>Optimize</b> the whole.</span><span class="page-num">4</span></footer>
  </section>

  <section class="slide s-questions">
    <h2 class="q-head">Ques-<br>tions?</h2>
    <svg class="q-device" width="92" height="62" viewBox="0 0 92 62"><rect x="10" y="2" width="72" height="48" rx="3" fill="none" stroke="rgba(255,255,255,.75)" stroke-width="3"/><path d="M2 52 h88 l-4 7 h-80 z" fill="none" stroke="rgba(255,255,255,.75)" stroke-width="3"/><text x="46" y="29" text-anchor="middle" fill="#fff" font-size="6" font-family="Montserrat,sans-serif">tallowcrest.com</text></svg>
    <ul class="q-contacts">
      <li><span class="q-icon"></span><div><b>FEEDBACK VIA</b><span>jane.doe@tallowcrest.com</span></div></li>
      <li><span class="q-icon"></span><div><b>FOLLOW TALLOW CREST</b><span>@tallowcrest</span></div></li>
      <li><span class="q-icon"></span><div><b>FOLLOW ONLINE</b><span>network.example/tallowcrest</span></div></li>
    </ul>
  </section>

</main>
</body>
</html>
```